Brand New Church Business Card Design. Needs to appeal to high school students, professionals.

Business Card. Bold lines and colors. Simple font. This is a new church looking to attract new families who have moved to the area. Business professionals mostly. have a working logo. may need a little tweaking. Church is designed to do excellent ministries for students and children. Like business card design in box on mark vault homepage. Want a front and back side. Prefer colors to match the logo. But will lean on designers preferences and wisdom. DO NOT WANT A CROSS OR RELIGIOUS SYMBOL on the card.

Target Market(s)

Families, Professionals, Students

Industry/Entity Type

High School

Contact Information for Business Card

SaltRock ChurchSaltRock.atForrest Coulter904-515-8349Forrest@PineHollow.at

Font styles to use
Sans Serif

Colors
0255a3
ffffff

Requirements
Must have
• Bold colors. Very Masculine. Creative
Nice to have
• On printnook.markvault.com homepage in the business card design box. the card with the black, blue and gray looks really sharp. matches our logos.
Should not have
• no crosses or religious symbols.

```html
<!DOCTYPE html>
<html lang="en">
<head>
<meta charset="utf-8">
<title>PineHollow Church – Business Card</title>
<link href="https://fonts.googleapis.com/css2?family=Arimo:wght@400;700&display=swap" rel="stylesheet">
<style>
  :root {
    --brand-blue: #2a8fd0;
    --deep-blue: #0255a3;
    --ink: #050505;
    --paper: #ffffff;
    --paper-shade: #d9d9d9;
    --backdrop: #e9e9e9;
  }
  html, body {
    margin: 0;
    padding: 0;
    width: 1200px;
    height: 885px;
    overflow: hidden;
    background: var(--backdrop);
    font-family: "Arimo", Arial, sans-serif;
  }
  .canvas {
    position: relative;
    width: 1200px;
    height: 885px;
  }
  .card {
    position: absolute;
    left: 250px;
    width: 700px;
    height: 400px;
    border-radius: 22px;
    overflow: hidden;
    box-shadow: 0 10px 28px rgba(0,0,0,0.25);
  }
  .card-front { top: 30px; }
  .card-back { top: 455px; }
  .card svg.bg {
    position: absolute;
    inset: 0;
    width: 100%;
    height: 100%;
  }
  .brand {
    position: absolute;
    display: flex;
    align-items: center;
    gap: 14px;
  }
  .brand-dot {
    border-radius: 50%;
    background: var(--brand-blue);
    flex: none;
  }
  .brand-name {
    font-weight: 700;
    color: var(--paper);
    line-height: 1;
  }
  .front-brand { top: 78px; right: 96px; }
  .front-brand .brand-dot { width: 92px; height: 92px; }
  .front-brand .brand-name { font-size: 38px; }

  .contact {
    position: absolute;
    left: 112px;
    top: 222px;
    color: var(--paper);
  }
  .contact-name {
    margin: 0;
    font-size: 30px;
    font-weight: 700;
    color: var(--brand-blue);
  }
  .contact-role {
    margin: 4px 0 18px;
    font-size: 22px;
  }
  .contact-list {
    list-style: none;
    margin: 0;
    padding: 0;
    font-size: 21px;
  }
  .contact-list li {
    display: flex;
    align-items: center;
    gap: 12px;
    margin-bottom: 6px;
  }
  .icon {
    width: 24px;
    height: 24px;
    border-radius: 5px;
    background: var(--brand-blue);
    display: flex;
    align-items: center;
    justify-content: center;
  }
  .icon svg { width: 16px; height: 16px; }

  .back-brand {
    top: 50%;
    left: 50%;
    transform: translate(-50%, -50%);
    flex-direction: column;
    gap: 18px;
  }
  .back-brand .brand-dot { width: 200px; height: 200px; }
  .back-brand .brand-name { font-size: 34px; color: var(--brand-blue); }
</style>
</head>
<body>
<main class="canvas">

  <section class="card card-front" aria-label="Card front">
    <svg class="bg" viewBox="0 0 700 400" preserveAspectRatio="none" aria-hidden="true">
      <rect width="700" height="400" fill="var(--deep-blue)"/>
      <rect width="700" height="400" fill="var(--brand-blue)" opacity="0.55"/>
      <ellipse cx="350" cy="200" rx="368" ry="338" fill="var(--paper)"/>
      <ellipse cx="350" cy="200" rx="360" ry="332" fill="var(--ink)"/>
    </svg>

    <div class="brand front-brand">
      <span class="brand-dot"></span>
      <span class="brand-name">PineHollow Church</span>
    </div>

    <div class="contact">
      <p class="contact-name">Dwayne Pellish</p>
      <p class="contact-role">Pastor</p>
      <ul class="contact-list">
        <li>
          <span class="icon">
            <svg viewBox="0 0 16 16" aria-hidden="true"><path d="M4 1.5l2.3 3-1.4 1.6c.8 1.8 2.3 3.3 4 4.1l1.6-1.4 3 2.3-1.3 2.4C7 13.2 2.8 9 2 3z" fill="#fff"/></svg>
          </span>
          904-555-0172
        </li>
        <li>
          <span class="icon">
            <svg viewBox="0 0 16 16" aria-hidden="true"><rect x="1.5" y="3.5" width="13" height="9" fill="none" stroke="#fff" stroke-width="1.5"/><path d="M1.5 3.5L8 9l6.5-5.5" fill="none" stroke="#fff" stroke-width="1.5"/></svg>
          </span>
          Dwayne@PineHollow.at
        </li>
        <li>
          <span class="icon">
            <svg viewBox="0 0 16 16" aria-hidden="true"><circle cx="8" cy="8" r="6.2" fill="none" stroke="#fff" stroke-width="1.4"/><ellipse cx="8" cy="8" rx="2.6" ry="6.2" fill="none" stroke="#fff" stroke-width="1.2"/><path d="M1.8 8h12.4" stroke="#fff" stroke-width="1.2"/></svg>
          </span>
          www.PineHollow.at
        </li>
      </ul>
    </div>
  </section>

  <section class="card card-back" aria-label="Card back">
    <svg class="bg" viewBox="0 0 700 400" preserveAspectRatio="none" aria-hidden="true">
      <defs>
        <radialGradient id="paperGlow" cx="50%" cy="45%" r="65%">
          <stop offset="0" stop-color="var(--paper)"/>
          <stop offset="1" stop-color="var(--paper-shade)"/>
        </radialGradient>
      </defs>
      <rect width="700" height="400" fill="var(--ink)"/>
      <ellipse cx="350" cy="200" rx="368" ry="338" fill="var(--brand-blue)"/>
      <ellipse cx="350" cy="200" rx="362" ry="334" fill="url(#paperGlow)"/>
    </svg>

    <div class="brand back-brand">
      <span class="brand-dot"></span>
      <span class="brand-name">PineHollow Church</span>
    </div>
  </section>

</main>
</body>
</html>
```